New company website for Redfern Hollow Building Company

We're looking to build a new company website that customers can use to contact us, get quotes, view past projects (renovations, additions, new construction, etc.), & learn more about our business. We want to use WordPress for our website and have already purchased the Divi theme (by Quillmark Studio). Using that theme isn't required but we already have several examples of websites that we want to model our site after that use this theme. The "look" we're after is simple, light, & clean.

Target Market(s)

Residential remodeling, renovations, and new construction.

Industry/Entity Type

Residential Construction

Coding

Coded - Design and coding required

Number of Pages Required

5+ page

Font styles to use
Sans Serif

Colors
33a6d7
aaaaaa

Requirements
Must have
• We require the website to be coded using the Divi theme. We'll be upgrading the project to include this today or tomorrow.
• The navigation bar should be static & remain at the top of the page. When scrolling we'd like the logo & info in the nav bar to size down. Here's an example of a site that does this: https://tovamerihomes.example/
Nice to have
• In the gallery with pictures of our finished product/jobs, when you mouse over the image, we'd like there to be additional info that shows up. For example, look at this gallery: https://tovamerihomes.example/projectcategories/kitchens/ We'll add a name/location of the job like: "Garvey kitchen - Apex, N.C."
• If you go to this website: https://plinvorworks.example/ and scroll down to the pictures, we like how the picture moves and is interactive.

```html
<!DOCTYPE html>
<html lang="en">
<head>
<meta charset="utf-8">
<title>Start Planning Your Project – Redfern Hollow Building Company</title>
<link href="https://fonts.googleapis.com/css2?family=Exo+2:wght@400;500;600&family=Montserrat:wght@400;600;700&family=Open+Sans:wght@400;600&family=Lora:ital@1&display=swap" rel="stylesheet">
<style>
:root{
  --blue:#33a6d7;
  --blue-dark:#2a95c6;
  --grey:#aaaaaa;
  --heading-grey:#6f6f6f;
  --text:#666666;
  --line:#e3e3e3;
  --footer-bg:#ece9e6;
  --white:#ffffff;
}
*{box-sizing:border-box;margin:0;padding:0}
html,body{width:1200px;height:2273px;overflow:hidden;background:var(--white)}
body{font-family:"Open Sans",Arial,sans-serif;color:var(--text);position:relative}
.abs{position:absolute}

/* header */
.site-header{left:0;top:0;width:1200px;height:95px;background:var(--blue)}
.brand{left:38px;top:30px;color:var(--white);font-family:"Exo 2",sans-serif;font-weight:600;line-height:1;letter-spacing:.5px}
.brand .name{font-size:20px;display:block;text-transform:uppercase}
.brand .sub{font-size:10px;letter-spacing:3.2px;display:block;margin-top:2px;text-transform:uppercase}
.main-nav{left:317px;top:39px;display:flex;align-items:center;gap:14px;font-family:Montserrat,sans-serif;font-size:11px;color:var(--white);white-space:nowrap}
.main-nav .item{display:flex;align-items:center;gap:3px}
.main-nav .call{margin-left:22px;font-weight:700}
.cta{left:914px;top:29px;width:256px;height:36px;border:1.5px solid var(--white);color:var(--white);font-family:Montserrat,sans-serif;font-size:12px;font-weight:700;display:flex;align-items:center;justify-content:center;gap:8px}

/* hero */
.hero{left:0;top:95px;width:1200px;height:211px;background:linear-gradient(100deg,#3b3129 0%,#6b5b49 30%,#8d7b66 55%,#6c6255 80%,#4a3e34 100%)}
.hero-title{left:120px;top:150px;font-family:"Exo 2",sans-serif;font-weight:500;font-size:46px;color:var(--white);letter-spacing:.5px;line-height:1}
.hero-text{left:120px;top:207px;width:470px;font-size:14px;line-height:18px;color:var(--white)}

/* form section */
.form-mist{left:0;top:306px;width:600px;height:600px;background:radial-gradient(ellipse at 20% 20%,#ececec 0%,rgba(255,255,255,0) 65%)}
.section-title{font-family:"Exo 2",sans-serif;font-weight:500;font-size:36px;color:var(--heading-grey);line-height:1;letter-spacing:.5px}
.section-title em{font-style:normal;color:var(--blue)}
.rule{height:3px;width:48px;background:var(--blue)}
.field{left:120px;width:421px;height:39px;border:1px solid var(--line);background:var(--white);font-size:14px;color:#777;padding:0 20px;display:flex;align-items:center;justify-content:space-between}
.field.active{border-color:var(--blue);color:var(--blue)}
.field .caret{width:22px;height:100%;border-left:1px solid var(--line);display:flex;align-items:center;justify-content:center;margin-right:-20px}
.field.message{align-items:flex-start;padding-top:12px;height:136px}
.checkbox-row{left:118px;top:1134px;display:flex;align-items:center;gap:14px;font-size:14px;color:#777}
.checkbox-row .box{width:24px;height:24px;border:1px solid var(--line)}
.submit{left:120px;top:1191px;width:195px;height:44px;background:var(--blue);color:var(--white);font-family:"Exo 2",sans-serif;font-weight:500;font-size:20px;display:flex;align-items:center;justify-content:center;letter-spacing:.5px}

.tips{left:609px;top:495px;width:470px;height:703px;background:linear-gradient(160deg,#6a6460 0%,#4a3f38 40%,#5d5a58 70%,#8a8a88 100%)}
.tips-title{left:609px;top:600px;width:450px;text-align:center;font-family:"Exo 2",sans-serif;font-weight:500;font-size:32px;line-height:45px;color:var(--white);letter-spacing:.5px}
.tips-list{left:689px;top:734px;width:320px;list-style:none}
.tips-list li{display:flex;gap:14px;margin-bottom:18px;font-family:Lora,serif;font-style:italic;font-size:14px;line-height:18px;color:var(--white)}
.tips-list svg{flex:none;margin-top:2px}

/* process */
.process-title{left:0;top:1397px;width:1200px;text-align:center}
.process-rule{left:576px;top:1474px}
.step-circle{width:78px;height:78px;border-radius:50%;background:var(--white);box-shadow:0 2px 10px rgba(0,0,0,.12);display:flex;align-items:center;justify-content:center;font-family:Montserrat,sans-serif;font-size:28px;font-weight:600;color:#d0d0d0;top:1518px}
.step-circle.current{background:var(--blue);color:var(--white);box-shadow:none}
.step-name{top:1623px;width:210px;text-align:center;font-family:Montserrat,sans-serif;font-weight:600;font-size:18px;color:#c3c3c3}
.step-text{top:1652px;width:200px;text-align:center;font-size:14px;line-height:18px;color:#c9c9c9}
.step-card{left:485px;top:1606px;width:229px;height:166px;border:2px solid var(--blue);background:var(--white);box-shadow:0 2px 8px rgba(0,0,0,.1)}
.step-card .step-name{position:static;width:auto;color:var(--blue);margin-top:15px}
.step-card .step-text{position:static;width:auto;color:var(--text);padding:0 20px;margin-top:10px}
.dots{left:576px;top:1822px;display:flex;gap:6px;align-items:center}
.dots i{width:8px;height:8px;border:1px solid #888;border-radius:50%}
.dots i.on{width:12px;height:12px;background:var(--blue);border-color:var(--blue)}

/* footer */
.site-footer{left:0;top:1918px;width:1200px;height:302px;background:var(--footer-bg)}
.footer-col{top:1990px;font-family:Montserrat,sans-serif;font-size:11px;color:#666;line-height:18px}
.footer-col h4{font-size:11px;font-weight:700;color:#555;margin-bottom:14px}
.footer-col .contact-line{display:flex;gap:10px}
.footer-brand{left:0;top:2150px;width:1200px;text-align:center;font-family:"Exo 2",sans-serif;font-weight:600;color:#8a8a8a;line-height:1}
.footer-brand .name{font-size:18px;display:block;text-transform:uppercase}
.footer-brand .sub{font-size:9px;letter-spacing:3px;display:block;margin-top:2px;text-transform:uppercase}
.bottom-bar{left:0;top:2220px;width:1200px;height:53px;background:var(--blue);font-family:Montserrat,sans-serif;font-size:11px;color:var(--white)}
.bottom-bar .copy{left:120px;top:20px}
.bottom-bar .portal{left:485px;top:20px;font-weight:700}
.bottom-bar .social-label{left:867px;top:20px;font-weight:700}
.social{left:960px;top:14px;display:flex;gap:8px}
.social i{width:24px;height:24px;border:1.5px solid var(--white);border-radius:50%}
</style>
</head>
<body>

<header class="abs site-header">
  <div class="abs brand"><span class="name">Redfern Hollow</span><span class="sub">Building Company</span></div>
  <nav class="abs main-nav">
    <span class="item">Getting Started<svg width="8" height="6" viewBox="0 0 8 6"><path d="M1 1l3 3 3-3" stroke="#fff" stroke-width="1.4" fill="none"/></svg></span>
    <span class="item">Who We Are<svg width="8" height="6" viewBox="0 0 8 6"><path d="M1 1l3 3 3-3" stroke="#fff" stroke-width="1.4" fill="none"/></svg></span>
    <span class="item">Specialties<svg width="8" height="6" viewBox="0 0 8 6"><path d="M1 1l3 3 3-3" stroke="#fff" stroke-width="1.4" fill="none"/></svg></span>
    <span class="item">Portfolio<svg width="8" height="6" viewBox="0 0 8 6"><path d="M1 1l3 3 3-3" stroke="#fff" stroke-width="1.4" fill="none"/></svg></span>
    <span class="item">Contact Us<svg width="8" height="6" viewBox="0 0 8 6"><path d="M1 5l3-3 3 3" stroke="#fff" stroke-width="1.4" fill="none"/></svg></span>
    <span class="call">Call : (555) 014 2276</span>
  </nav>
  <div class="abs cta">START PLANNING YOUR PROJECT<svg width="9" height="6" viewBox="0 0 9 6"><path d="M1 1l3.5 3.5L8 1" stroke="#fff" stroke-width="1.5" fill="none"/></svg></div>
</header>

<div class="abs hero" role="img" aria-label="Photo of a finished kitchen with tiled backsplash and sink"></div>
<h1 class="abs hero-title">START PLANNING YOUR PROJECT</h1>
<p class="abs hero-text">Lorem ipsum dolor sit amet, consectetur adipiscing, sed do eiusmod tempor incididunt ut labore et dolore magna aliqua.</p>

<div class="abs form-mist"></div>
<h2 class="abs section-title" style="left:120px;top:398px">PROJECT <em>FORM</em></h2>
<div class="abs rule" style="left:120px;top:457px"></div>

<div class="abs field active" style="top:494px">First &amp; Last Name</div>
<div class="abs field" style="top:542px">Phone No.</div>
<div class="abs field" style="top:590px">Email</div>
<div class="abs field" style="top:638px">Project Address</div>
<div class="abs field" style="top:686px">Project Zip Code</div>
<div class="abs field" style="top:734px">Project Type<span class="caret"><svg width="9" height="6" viewBox="0 0 9 6"><path d="M0 0h9L4.5 6z" fill="#ddd"/></svg></span></div>
<div class="abs field" style="top:782px">Do you have a vison for your project<span class="caret"><svg width="9" height="6" viewBox="0 0 9 6"><path d="M0 0h9L4.5 6z" fill="#ddd"/></svg></span></div>
<div class="abs field" style="top:830px">Have you remodeled before ?<span class="caret"><svg width="9" height="6" viewBox="0 0 9 6"><path d="M0 0h9L4.5 6z" fill="#ddd"/></svg></span></div>
<div class="abs field" style="top:878px">How did you hear about us?<span class="caret"><svg width="9" height="6" viewBox="0 0 9 6"><path d="M0 0h9L4.5 6z" fill="#ddd"/></svg></span></div>
<div class="abs field" style="top:926px">Person who referred me</div>
<div class="abs field message" style="top:979px">Best weekday &amp; time yo reach you</div>
<div class="abs checkbox-row"><span class="box"></span>Add me to your list for design inspiration</div>
<div class="abs submit">SUBMIT</div>

<div class="abs tips" role="img" aria-label="Photo of a kitchen with pendant lights, marble island and dark cabinets"></div>
<h3 class="abs tips-title">TIPS FOR HOW<br>TO PLAN</h3>
<ul class="abs tips-list">
  <li><svg width="20" height="20" viewBox="0 0 20 20"><circle cx="10" cy="10" r="9.5" fill="#fff"/><path d="M5.5 10.5l3 3 6-6.5" stroke="#555" stroke-width="2" fill="none"/></svg>Excepteur sint occaecat cupidatat non proident, sunt in culpa qui deserunt.</li>
  <li><svg width="20" height="20" viewBox="0 0 20 20"><circle cx="10" cy="10" r="9.5" fill="#fff"/><path d="M5.5 10.5l3 3 6-6.5" stroke="#555" stroke-width="2" fill="none"/></svg>Ut enim ad minim veniam, laboris nisi ut aliquip commodo consequat.</li>
  <li><svg width="20" height="20" viewBox="0 0 20 20"><circle cx="10" cy="10" r="9.5" fill="#fff"/><path d="M5.5 10.5l3 3 6-6.5" stroke="#555" stroke-width="2" fill="none"/></svg>Duis aute irure &nbsp;dolor in reprehenderit in voluptate velit esse cillum dolore .</li>
  <li><svg width="20" height="20" viewBox="0 0 20 20"><circle cx="10" cy="10" r="9.5" fill="#fff"/><path d="M5.5 10.5l3 3 6-6.5" stroke="#555" stroke-width="2" fill="none"/></svg>Excepteur sint occaecat cupidatat non proident, sunt in culpa qui officia deserunt.</li>
  <li><svg width="20" height="20" viewBox="0 0 20 20"><circle cx="10" cy="10" r="9.5" fill="#fff"/><path d="M5.5 10.5l3 3 6-6.5" stroke="#555" stroke-width="2" fill="none"/></svg>Ut enim ad minim veniam, laboris nisi ut aliquip commodo consequat.</li>
</ul>

<h2 class="abs section-title process-title">OUR <em>PROCESS</em></h2>
<div class="abs rule process-rule"></div>

<svg class="abs" style="left:0;top:1545px" width="1200" height="24" viewBox="0 0 1200 24">
  <g fill="none" stroke-width="2">
    <line x1="215" y1="12" x2="313" y2="12" stroke="#2a7fa8"/>
    <circle cx="318" cy="12" r="4.5" stroke="#2a7fa8" fill="#fff"/>
    <line x1="439" y1="12" x2="537" y2="12" stroke="#2a7fa8"/>
    <circle cx="542" cy="12" r="4.5" stroke="#2a7fa8" fill="#fff"/>
    <line x1="660" y1="12" x2="756" y2="12" stroke="#2a7fa8"/>
    <circle cx="761" cy="12" r="4.5" stroke="#2a7fa8" fill="#fff"/>
    <line x1="877" y1="12" x2="975" y2="12" stroke="#9cc9df"/>
    <circle cx="980" cy="12" r="4.5" stroke="#9cc9df" fill="#fff"/>
  </g>
</svg>
<div class="abs step-circle" style="left:122px">01</div>
<div class="abs step-circle" style="left:338px">02</div>
<div class="abs step-circle current" style="left:561px">03</div>
<div class="abs step-circle" style="left:781px">04</div>
<div class="abs step-circle" style="left:999px">05</div>

<div class="abs step-name" style="left:55px">Initial Meetings</div>
<p class="abs step-text" style="left:60px">Lorem ipsum dolor sit amet, consectetur adipiscing</p>
<div class="abs step-name" style="left:271px">Design Phase</div>
<p class="abs step-text" style="left:276px">Lorem ipsum dolor sit amet, consectetur adipiscing,</p>
<div class="abs step-card">
  <div class="step-name">Construction Phase</div>
  <p class="step-text">Lorem ipsum dolor sit amet, consectetur adipiscing, sed do eiusmod tempor incididunt ut labore et dolore magna aliqua.</p>
</div>
<div class="abs step-name" style="left:715px">Warranty</div>
<p class="abs step-text" style="left:720px">Lorem ipsum dolor sit amet, consectetur adipiscing,</p>
<div class="abs step-name" style="left:933px">Initial Meetings</div>
<p class="abs step-text" style="left:938px">Lorem ipsum dolor sit amet, consectetur adipiscing,</p>

<div class="abs dots"><i></i><i></i><i class="on"></i><i></i><i></i></div>

<footer class="abs site-footer"></footer>
<div class="abs footer-col" style="left:120px"><h4>Getting Started</h4>Our Process<br>What to Expect<br>FAQs</div>
<div class="abs footer-col" style="left:265px"><h4>Who We Are</h4>Our story<br>Redfern Hollow Team<br>Testimonials</div>
<div class="abs footer-col" style="left:414px"><h4>Specialties</h4>Remodeling<br>New Home Construction<br>Additions</div>
<div class="abs footer-col" style="left:615px"><h4>Portfolio</h4>Before and after<br>Kitchens<br>Bathrooms<br>Whole house</div>
<div class="abs footer-col" style="left:771px"><h4>Contact Us</h4>Contact form<br>Link to SiteLedger</div>
<div class="abs footer-col" style="left:926px"><h4>Contact Us</h4>
  <div class="contact-line"><svg width="11" height="18" viewBox="0 0 11 18"><rect x="0" y="5" width="11" height="8" fill="#777"/><path d="M0 5l5.5 4.5L11 5" stroke="#ece9e6" fill="none"/></svg><span>Address<br>48 Larkmoor Lane,<br>Suite B, Fenwick, NC 27099</span></div>
  <div class="contact-line" style="margin-top:10px"><svg width="11" height="18" viewBox="0 0 11 18"><path d="M2 4c-1 1-1 3 1 6s4 4 5.5 3.5l1-1.5-2-1.5-1 1C5.5 11 4 9 3.8 8l1-1-1.3-2.2z" fill="#777"/></svg><span>555.014.2276</span></div>
</div>
<div class="abs footer-brand"><span class="name">Redfern Hollow</span><span class="sub">Building Company</span></div>

<div class="abs bottom-bar">
  <span class="abs copy">© 2018 &nbsp;Redfern Hollow Building Company, Legal &amp; Privacy</span>
  <span class="abs portal">Client Portal : portal.siteledger.example</span>
  <span class="abs social-label">Social Activity</span>
  <div class="abs social"><i></i><i></i><i></i><i></i></div>
</div>

</body>
</html>
```